GLP letterhead

We need a letterhead design for our new company based in Los Angeles called "Gold Ladder Pictures". We develop film and television projects. We work with investors, financiers, film production companies, film distribution and sales companies as well as studios. We would like to incorporate our logo (see attached) but make the letterhead simple and elegant. We need to include: logo, company address, phone number and company website.
Updates

Hello designers, Thanks for your submissions. For our letterhead, we are looking for something more simple and elegant. No heavy bars or lines. Make it feel light and clean. Not a lot of ink on the page. Use the logo and contact info but think "clean", "streamlined" and mostly white paper. Looking forward to seeing more... thanks! Gold Ladder Pictures team

Target Market(s)

Studio executives, talent agents and agencies, financiers, investors.

Industry/Entity Type

It Company

Requirements
Must have
• Gold Ladder Pictures logo (see attached). Logo may be cropped and altered appropriately for elegant letterhead design.
• Please include:
• COMPANY ADDRESS:
• TQV Media Campus
• 2750 Halvering Avenue
• Norwick Center, 4th Floor
• Farrowdale Cove, CA 90999
• COMPANY WEBSITE:
• www.goldladderpicturesgroup.example
• COMPANY PHONE NUMBER:
• 555-014-2236

```html
<!DOCTYPE html>
<html lang="en">
<head>
<meta charset="utf-8">
<title>Gold Ladder Pictures Letterhead</title>
<link rel="stylesheet" href="https://fonts.googleapis.com/css2?family=Dosis:wght@400;500;700&display=swap">
<style>
  :root {
    --teal: #2a525b;
    --ink: #1f1f21;
    --accent: #2ea7d8;
    --paper: #ffffff;
    --on-dark: #ffffff;
    --muted: #5a6f74;
  }
  html, body {
    margin: 0;
    padding: 0;
    width: 1063px;
    height: 1200px;
    overflow: hidden;
    background: var(--paper);
  }
  .letterhead {
    position: relative;
    width: 1063px;
    height: 1200px;
    background: var(--paper);
    font-family: "Dosis", "Arial Narrow", sans-serif;
  }
  .header-band {
    position: absolute;
    top: 0;
    left: 0;
    width: 1063px;
    height: 110px;
    display: block;
  }
  .brand {
    position: absolute;
    top: 14px;
    left: 0;
    width: 1063px;
    text-align: center;
    color: var(--accent);
  }
  .brand-dot {
    width: 30px;
    height: 30px;
    border-radius: 50%;
    background: var(--accent);
    margin: 0 auto 7px;
  }
  .brand-name {
    font-weight: 700;
    font-size: 15px;
    letter-spacing: 2px;
    text-transform: uppercase;
    line-height: 1.1;
  }
  .brand-tagline {
    font-weight: 500;
    font-size: 7px;
    letter-spacing: 1.5px;
    color: var(--on-dark);
    text-transform: uppercase;
    margin-top: 4px;
  }
  .footer {
    position: absolute;
    left: 80px;
    right: 80px;
    bottom: 34px;
    padding-top: 14px;
    border-top: 1px solid var(--teal);
    color: var(--muted);
    font-size: 15px;
    font-weight: 400;
    display: flex;
    flex-direction: column;
    align-items: center;
    gap: 6px;
  }
  .contact-line {
    display: flex;
    align-items: center;
    gap: 22px;
    white-space: nowrap;
  }
  .contact-item {
    display: inline-flex;
    align-items: center;
    gap: 7px;
  }
  .contact-icon {
    width: 12px;
    height: 12px;
    fill: var(--teal);
  }
  .at-mark {
    color: var(--teal);
    font-weight: 500;
  }
</style>
</head>
<body>
<main class="letterhead">
  <svg class="header-band" viewBox="0 0 1063 110" aria-hidden="true">
    <rect x="0" y="0" width="1063" height="6" fill="var(--teal)"/>
    <path d="M330 0 H733 C700 0 688 30 660 60 C632 88 590 98 531 98 C472 98 430 88 402 60 C374 30 362 0 330 0 Z" fill="var(--ink)"/>
  </svg>

  <header class="brand">
    <div class="brand-dot"></div>
    <div class="brand-name">Gold Ladder Pictures</div>
    <div class="brand-tagline">A Media Entertainment Company</div>
  </header>

  <footer class="footer">
    <div class="contact-line">
      <span class="contact-item">
        <svg class="contact-icon" viewBox="0 0 12 16"><path d="M6 0C2.7 0 0 2.6 0 5.9 0 10 6 16 6 16s6-6 6-10.1C12 2.6 9.3 0 6 0zm0 8.2A2.3 2.3 0 1 1 6 3.6a2.3 2.3 0 0 1 0 4.6z"/></svg>
        TQV Media Campus, 2750 Halvering Avenue, Norwick Center, 4th Floor, Farrowdale Cove, CA 90999
      </span>
    </div>
    <div class="contact-line">
      <span class="contact-item"><span class="at-mark">@</span> 555-014-2236</span>
      <span class="contact-item">
        <svg class="contact-icon" viewBox="0 0 10 16"><path d="M1.5 0h7A1.5 1.5 0 0 1 10 1.5v13A1.5 1.5 0 0 1 8.5 16h-7A1.5 1.5 0 0 1 0 14.5v-13A1.5 1.5 0 0 1 1.5 0zM1.5 2v10h7V2zM5 13a1 1 0 1 0 0 2 1 1 0 0 0 0-2z"/></svg>
        jordan@goldladderpicturesgroup.example
      </span>
      <span class="contact-item">
        <svg class="contact-icon" viewBox="0 0 16 16"><path d="M8 0a8 8 0 1 0 0 16A8 8 0 0 0 8 0zm5.9 7h-2.6a12 12 0 0 0-1-4.6A6 6 0 0 1 13.9 7zM8 2c.7.9 1.2 2.7 1.3 5H6.7C6.8 4.7 7.3 2.9 8 2zM5.7 2.4a12 12 0 0 0-1 4.6H2.1a6 6 0 0 1 3.6-4.6zM2.1 9h2.6a12 12 0 0 0 1 4.6A6 6 0 0 1 2.1 9zM8 14c-.7-.9-1.2-2.7-1.3-5h2.6c-.1 2.3-.6 4.1-1.3 5zm2.3-.4a12 12 0 0 0 1-4.6h2.6a6 6 0 0 1-3.6 4.6z"/></svg>
        www.goldladderpicturesgroup.example
      </span>
    </div>
  </footer>
</main>
</body>
</html>
```